Fashion Design Business Card

I need a new business card designed for a new fashion company. I have attached what I have currently designed. I want it more feminine looking, the logo needs to be gold. I want it simple, feminine and stylish. Please give me some different ideas with the fonts.
Updates

I need to send the design we currently have, as we have worked out the logo.
You also need all of our details
Industry/Entity Type
Fashion
Look and feel
Each slider illustrates characteristics of the customer's brand and the style your logo design should communicate.

```html
<!DOCTYPE html>
<html lang="en">
<head>
<meta charset="utf-8">
<title>Mirela Hartwell – Business Card</title>
<link rel="stylesheet" href="https://fonts.googleapis.com/css2?family=Marcellus&display=swap">
<style>
  :root {
    --page-bg: #ffffff;
    --card-bg: #ffffff;
    --card-border: #1a1a1a;
    --ink: #1e1e1e;
    --gold: #e3d91c;
    --gold-pale: #f6f2b0;
    --gold-mist: #fbf9e0;
  }
  * { box-sizing: border-box; margin: 0; padding: 0; }
  html, body {
    width: 1200px;
    height: 900px;
    overflow: hidden;
    background: var(--page-bg);
  }
  body {
    position: relative;
    font-family: "Marcellus", serif;
    color: var(--ink);
  }
  .card {
    position: absolute;
    left: 452px;
    width: 326px;
    height: 218px;
    background: var(--card-bg);
    border: 1.5px solid var(--card-border);
    overflow: hidden;
  }
  .card--front { top: 219px; }
  .card--back  { top: 474px; }

  .flourish {
    position: absolute;
    border-radius: 50%;
    background: radial-gradient(ellipse at 50% 60%, var(--gold-pale) 0%, var(--gold-mist) 55%, rgba(255,255,255,0) 75%);
  }
  .brand-dot {
    position: absolute;
    border-radius: 50%;
    background: var(--gold);
  }

  .card--front .flourish { left: 10px; top: 4px; width: 120px; height: 62px; }
  .card--front .brand-dot { left: 58px; top: 16px; width: 24px; height: 24px; }

  .card--back .flourish { left: 13px; top: 4px; width: 300px; height: 162px; }
  .card--back .brand-dot { left: 123px; top: 46px; width: 80px; height: 80px; }

  .holder-name {
    position: absolute;
    left: 0;
    right: 0;
    text-align: center;
    font-weight: 400;
    letter-spacing: 0.4px;
    white-space: nowrap;
  }
  .card--front .holder-name { top: 83px; font-size: 21px; }
  .card--back .holder-name  { top: 172px; font-size: 29px; }

  .holder-role {
    position: absolute;
    left: 0;
    right: 0;
    top: 116px;
    text-align: center;
    font-size: 14px;
  }
  .contact {
    position: absolute;
    right: 6px;
    bottom: 5px;
    text-align: right;
    font-size: 14px;
    line-height: 18px;
    list-style: none;
    white-space: nowrap;
  }
</style>
</head>
<body>
  <section class="card card--front" aria-label="Business card front">
    <div class="flourish" role="img" aria-label="Gold floral flourish ornament"></div>
    <span class="brand-dot"></span>
    <h1 class="holder-name">Mirela Hartwell</h1>
    <p class="holder-role">fashion designer</p>
    <ul class="contact">
      <li>ph. 0400531762</li>
      <li>e-mail: mirela@mirelahartwell.com</li>
      <li>web: www.mirelahartwell.com</li>
    </ul>
  </section>

  <section class="card card--back" aria-label="Business card back">
    <div class="flourish" role="img" aria-label="Large gold floral flourish ornament"></div>
    <span class="brand-dot"></span>
    <p class="holder-name">Mirela Hartwell</p>
  </section>
</body>
</html>
```